依頼詳細
現在、不動産業務にて空家・空地・相続させたお客様へお手紙と返信用ハガキをつけお送りしています。使用していますはがきデザインはワードで作成し、プリンターではがきに印刷しお手紙に添えてお送りしています。
返信いただくお客様に、
該当する内容に〇をつけていただき、送っていただいております。(2パターン使用中です)
お客様からの返信率はあまりない状況です。

※お客様の年齢層の幅も広いですし、相続対象者の方にもお送りしますので、お客様の中に はDMはがき自体を不快に思われる方もいらっしゃいますので、
デザインはシンプルなもので字体やバランスなどのご提案も含めお願いしたいです。
記載項目
裏面:ご回答書(ご所有の不動産について)、ご意見・ご要望、お客様のご住所・
お名前・ご連絡先
希望イメージ
シンプル 複雑
単色 カラフル
暗い 明るい
日常 高級
遊び心 厳粛
未来的 伝統的
女性的 男性的
希望する色
納品ファイル
• 高解像度JPG (.jpg)
• PNG形式 (.png)
補足説明
■ 選んだ理由

提案していただきありがとうございました。
見た瞬間から目を引かれるデザインで、柔らかい雰囲気がとても気に入りました。

■ 提案者全員のお礼・コメント

素晴らしいデザインでした!
ありがとうございました。

```html
<!DOCTYPE html>
<html lang="ja">
<head>
<meta charset="utf-8">
<title>ご所有の不動産についてのアンケート</title>
<link href="https://fonts.googleapis.com/css2?family=Noto+Sans+JP:wght@400;500;700&display=swap" rel="stylesheet">
<style>
  :root {
    --orange: #f08c1e;
    --orange-line: #f3a04a;
    --ink: #333333;
    --paper: #ffffff;
    --edge: #d6d6d6;
  }
  * { margin: 0; padding: 0; box-sizing: border-box; }
  html, body { width: 825px; height: 1200px; overflow: hidden; background: var(--paper); }
  body { font-family: "Noto Sans JP", sans-serif; color: var(--ink); }

  .card {
    position: relative;
    width: 825px; height: 1200px;
    border: 3px solid var(--edge);
    background: var(--paper);
  }

  .header {
    position: absolute;
    left: 20px; top: 20px; width: 779px; height: 230px;
    background: var(--orange);
    color: #fff;
    text-align: center;
  }
  .header .topic { font-size: 27px; font-weight: 500; margin-top: 20px; letter-spacing: 1px; }
  .header .title { font-size: 48px; font-weight: 700; margin-top: 4px; letter-spacing: 2px; }
  .header .lead { font-size: 22px; margin-top: 8px; }
  .header .note { position: absolute; right: 110px; bottom: 14px; font-size: 21px; }

  .choices {
    position: absolute;
    left: 132px; top: 268px;
    list-style: none;
  }
  .choices li {
    display: flex; align-items: center;
    height: 49px;
    font-size: 28px; font-weight: 500;
    letter-spacing: 1px;
  }
  .choices .box {
    width: 22px; height: 22px;
    border: 2px solid var(--ink);
    margin-right: 14px;
    flex: none;
  }

  .remarks {
    position: absolute;
    left: 128px; top: 648px; width: 590px;
    display: flex; justify-content: space-between;
    font-size: 30px;
  }

  .contact {
    position: absolute;
    left: 99px; top: 712px; width: 622px; height: 390px;
    border: 4px solid var(--orange);
    border-radius: 14px;
    display: grid;
    grid-template-columns: 135px 1fr;
    grid-template-rows: 158px 116px 1fr;
    overflow: hidden;
  }
  .contact .label {
    display: flex; flex-direction: column; align-items: center; justify-content: center;
    font-size: 21px; font-weight: 500;
    border-right: 3px solid var(--orange);
    line-height: 1.5;
  }
  .contact .label .kana { font-size: 14px; line-height: 1; margin-bottom: 4px; }
  .contact .field { position: relative; padding: 6px 14px; font-size: 24px; }
  .contact .row-top { border-bottom: 3px solid var(--orange); }
  .contact .name-field::after {
    content: ""; position: absolute; left: 0; right: 0; top: 36px;
    border-top: 2px dashed var(--orange-line);
  }

  .thanks {
    position: absolute;
    left: 154px; top: 1132px; width: 512px; height: 46px;
    background: var(--orange);
    border-radius: 23px;
    color: #fff;
    font-size: 20px;
    display: flex; align-items: center; justify-content: center;
    letter-spacing: 1px;
  }
</style>
</head>
<body>
<div class="card">
  <header class="header">
    <p class="topic">《ご所有の不動産について》</p>
    <h1 class="title">アンケートにご協力ください</h1>
    <p class="lead">該当する項目にチェックを入れてご返送ください。</p>
    <p class="note">（複数回答可）</p>
  </header>

  <ul class="choices">
    <li><span class="box"></span>売却してもよい</li>
    <li><span class="box"></span>売却するつもりはない</li>
    <li><span class="box"></span>どちらとも決めていない</li>
    <li><span class="box"></span>不動産の価値を知りたい</li>
    <li><span class="box"></span>当分様子を見て決める</li>
    <li><span class="box"></span>将来自分（子ども）が家を建てて住む予定</li>
    <li><span class="box"></span>不動産の活用を考えている</li>
    <li><span class="box"></span>その他ご意見、ご要望</li>
  </ul>

  <div class="remarks"><span>(</span><span>)</span></div>

  <div class="contact">
    <div class="label row-top">ご住所</div>
    <div class="field row-top">〒</div>
    <div class="label row-top"><span class="kana">ふりがな</span>お名前</div>
    <div class="field row-top name-field"></div>
    <div class="label">ご連絡先</div>
    <div class="field"></div>
  </div>

  <div class="thanks">アンケートのご協力ありがとうございました。</div>
</div>
</body>
</html>
```